Printable PDF Template for "Do it yourself" receipts needed

We need a reusable Template for PDF. Content is Do it yourself related.
Elements should be easy to exchange.

Here you can find some samples:
http://www.wundertagsfreude.de/downloads/bastelkiste/aus_muesliverpackung_wird_notizheft.pdf
http://www.wundertagsfreude.de/downloads/bastelkiste/teelichthalter_aus_plastikflasche.pdf
http://www.wundertagsfreude.de/downloads/bastelkiste/lampe_aus_getraenkekartons.pdf

Font styles to use
Decorative

```html
<!DOCTYPE html>
<html lang="de">
<head>
<meta charset="utf-8">
<title>DIY Vorlage</title>
<link rel="stylesheet" href="https://fonts.googleapis.com/css2?family=Kalam:wght@400;700&family=Open+Sans:wght@400&display=swap">
<style>
  :root {
    --wood-light: #dca76a;
    --wood-mid: #c98f52;
    --wood-dark: #b87a40;
    --paper: #ede7d7;
    --paper-edge: #d9d1bc;
    --burlap: #a2733f;
    --burlap-dark: #8a5f31;
    --title: #b4552a;
    --text: #6b5a48;
    --bullet: #c8783c;
    --photo: #5a4636;
    --photo-light: #7b6450;
    --frame: #fbf7ee;
    --white: #ffffff;
  }
  * { margin: 0; padding: 0; box-sizing: border-box; }
  html, body { width: 1200px; height: 849px; overflow: hidden; }
  body { background: var(--wood-mid); font-family: "Open Sans", sans-serif; }

  .canvas {
    position: relative;
    width: 1200px;
    height: 849px;
    overflow: hidden;
    background:
      repeating-linear-gradient(180deg,
        rgba(0,0,0,0.06) 0 2px, transparent 2px 96px),
      linear-gradient(90deg,
        var(--wood-light) 0 22%, var(--wood-mid) 22% 41%,
        var(--wood-light) 41% 63%, var(--wood-dark) 63% 64%,
        var(--wood-mid) 64% 82%, var(--wood-light) 82% 100%);
  }

  .torn-paper { position: absolute; filter: drop-shadow(0 3px 4px rgba(60,35,10,0.35)); }
  .torn-paper polygon { fill: var(--paper); stroke: var(--paper-edge); stroke-width: 1; }

  .burlap-label {
    position: absolute;
    background: linear-gradient(135deg, var(--burlap), var(--burlap-dark));
    box-shadow: 0 3px 6px rgba(40,20,5,0.4);
    display: flex; align-items: center; justify-content: center;
    color: var(--white);
    font-family: "Kalam", cursive;
    font-weight: 400;
  }

  .project-title {
    position: absolute;
    left: 52px; top: 182px;
    font-family: "Kalam", cursive;
    font-weight: 700;
    font-size: 43px;
    letter-spacing: 1.5px;
    color: var(--title);
  }

  .polaroid {
    position: absolute;
    background: var(--frame);
    box-shadow: 0 4px 10px rgba(40,20,5,0.4);
  }
  .polaroid-photo {
    position: absolute;
    background: radial-gradient(circle at 50% 50%, var(--photo-light), var(--photo) 75%);
    display: flex; align-items: center; justify-content: center;
    text-align: center;
    color: var(--white);
    font-family: "Kalam", cursive;
    font-weight: 400;
    line-height: 0.95;
  }

  .item-list {
    position: absolute;
    list-style: none;
    font-size: 13.5px;
    line-height: 1.25;
    color: var(--text);
  }
  .item-list li { position: relative; padding-left: 24px; }
  .item-list li::before {
    content: ""; position: absolute; left: 0; top: 4px;
    width: 9px; height: 9px; border-radius: 50%;
    background: var(--bullet);
  }
</style>
</head>
<body>
<main class="canvas">

  <!-- Material section paper -->
  <svg class="torn-paper" style="left:652px;top:88px" width="505" height="306" viewBox="0 0 505 306">
    <polygon points="6,14 60,8 110,12 170,4 230,10 290,3 350,9 410,2 460,8 498,4 492,60 500,120 494,180 502,240 496,298 440,292 380,300 320,294 260,302 200,296 140,300 80,294 20,300 4,250 10,190 2,130 8,70"/>
  </svg>

  <!-- Hilfsmittel section paper -->
  <svg class="torn-paper" style="left:658px;top:440px" width="490" height="352" viewBox="0 0 490 352">
    <polygon points="8,12 70,6 130,12 190,4 250,10 310,3 370,9 430,2 484,8 478,70 486,140 480,210 488,280 482,344 420,338 360,346 300,340 240,348 180,342 120,346 60,340 6,346 12,280 4,210 10,140 2,70"/>
  </svg>

  <!-- Main photo frame -->
  <div class="polaroid" style="left:62px;top:296px;width:492px;height:482px;transform:rotate(-2deg)">
    <div class="polaroid-photo" role="img" aria-label="Projektfoto: Blumenmuster in Braun- und Cremetönen"
         style="left:18px;top:6px;width:452px;height:396px;font-size:58px">Platz<br>für<br>Foto</div>
  </div>

  <!-- Title paper strip -->
  <svg class="torn-paper" style="left:0;top:112px" width="592" height="208" viewBox="0 0 592 208">
    <polygon points="0,12 40,6 90,14 140,4 200,12 260,2 320,10 380,4 440,12 500,6 560,10 588,4 584,60 590,120 580,176 540,186 500,178 460,196 420,182 380,200 340,184 300,196 260,180 220,198 180,184 140,200 100,186 60,196 20,186 0,192"/>
  </svg>

  <div class="burlap-label" style="left:30px;top:34px;width:218px;height:100px;transform:rotate(-3deg);justify-content:flex-start;padding-left:28px;font-size:42px">DIY</div>

  <h1 class="project-title">Titel des Projektes</h1>

  <!-- Material -->
  <div class="burlap-label" style="left:630px;top:62px;width:196px;height:136px;transform:rotate(-4deg)">
    <span style="font-size:34px;transform:rotate(-6deg);display:block">Material</span>
  </div>

  <ul class="item-list" style="left:735px;top:218px;transform:rotate(5deg)">
    <li style="margin-bottom:12px">Müslischachtel<br>oder Pizzakarton</li>
    <li style="margin-bottom:12px">weißes oder kariertes<br>Papier</li>
    <li>buntes Papier bzw.<br>Kreppapier</li>
  </ul>

  <div class="polaroid" style="left:934px;top:122px;width:190px;height:228px;transform:rotate(3deg)">
    <div class="polaroid-photo" role="img" aria-label="Foto der Materialien"
         style="left:10px;top:8px;width:170px;height:186px;font-size:30px;transform:rotate(6deg)">Platz<br>für<br>Foto</div>
  </div>

  <!-- Hilfsmittel -->
  <div class="burlap-label" style="left:622px;top:414px;width:218px;height:150px;transform:rotate(2deg)">
    <span style="font-size:33px;transform:rotate(-10deg);display:block">Hilfsmittel</span>
  </div>

  <ul class="item-list" style="left:735px;top:602px;transform:rotate(-4deg)">
    <li style="margin-bottom:10px">Nadel und Faden</li>
    <li style="margin-bottom:10px">Schere</li>
    <li style="margin-bottom:10px">Klebestift</li>
    <li style="margin-bottom:10px">Knopf</li>
    <li>evtl. Washi Tape</li>
  </ul>

  <div class="polaroid" style="left:904px;top:378px;width:202px;height:230px;transform:rotate(-9deg)">
    <div class="polaroid-photo" role="img" aria-label="Foto der Hilfsmittel"
         style="left:10px;top:8px;width:182px;height:188px;font-size:30px;transform:rotate(12deg)">Platz<br>für<br>Foto</div>
  </div>

  <div class="polaroid" style="left:948px;top:592px;width:206px;height:168px;transform:rotate(14deg)">
    <div class="polaroid-photo" role="img" aria-label="Foto eines Arbeitsschritts"
         style="left:10px;top:8px;width:186px;height:132px;font-size:30px;transform:rotate(6deg)">Platz<br>für<br>Foto</div>
  </div>

</main>
</body>
</html>
```